KVAP Property Flyer - For Support Coordinators

Revamping our current brochures and social media posts for our properties. We need a clearer, simpler design that would be designed for Support Coordinators. Attached is our current brochure for reference.

Key details to highlight would include:
- Type of property: Studio Apartments with Psychosocial Disability Support located in Inner West
- Accommodation features
- Services

Our logo is also attached, please make the brochure with similar branding colours and fonts.

Designs look the same

Sick

Font styles to use
Sans Serif
Other font styles liked:
• Montserrat Light and Montserrat Semi Bold

Colors
0054AA
0677BA
7BADD7
CADEEF
E8F1F8

Requirements
Nice to have
• Please refer to this style guide: https://slides.trovelmark.com/deck/8TkwPzLmRd5VbQx2NcYh4GfJs7AeUo9WiKnBrMp3tZq/view?mode=shared

```html
<!DOCTYPE html>
<html lang="en">
<head>
<meta charset="utf-8">
<title>Harbour Kind Living – Elmsbury Studio Apartments</title>
<link href="https://fonts.googleapis.com/css2?family=Crimson+Text:wght@600&family=Lato:wght@400&family=Montserrat:wght@300&display=swap" rel="stylesheet">
<style>
  :root{
    --backdrop:#5e5e5e;
    --paper:#ffffff;
    --band:#4ea5cb;
    --band-deep:#3f98c2;
    --cyan:#b7e3eb;
    --cyan-soft:#d9f0f4;
    --title:#3b9ac5;
    --ink:#1e1e1e;
    --brand-grey:#5b6670;
    --footer:#59aad0;
  }
  *{box-sizing:border-box;margin:0;padding:0}
  html,body{width:1200px;height:1200px;overflow:hidden;background:var(--backdrop)}
  body{position:relative;font-family:'Lato',sans-serif;color:var(--ink)}
  .page{position:absolute;top:233px;width:570px;height:734px;background:var(--paper);overflow:hidden}
  .page--front{left:22px}
  .page--back{left:605px}
  .page-art{position:absolute;inset:0;width:570px;height:734px}

  /* front */
  .brand-name{position:absolute;font-family:'Montserrat',sans-serif;font-weight:300;letter-spacing:2px;white-space:nowrap}
  .front-brand{left:326px;top:120px;font-size:16px;color:var(--brand-grey)}
  .welcome{position:absolute;left:228px;top:606px;font-family:'Crimson Text',serif;font-weight:600;font-size:21px;letter-spacing:.6px;color:var(--title);text-transform:uppercase}
  .welcome-copy{position:absolute;left:210px;top:640px;width:336px;font-size:8.6px;line-height:10.8px}
  .welcome-copy p+p{margin-top:4px}

  /* back */
  .section-band{position:absolute;left:0;height:24px;background:var(--band);color:#fff;font-family:'Crimson Text',serif;font-weight:600;font-size:20px;line-height:24px;padding-left:17px;letter-spacing:.4px;clip-path:polygon(0 0,100% 0,calc(100% - 6px) 100%,0 100%);white-space:nowrap}
  .band-communities{top:52px;width:319px;text-transform:uppercase}
  .band-features{top:145px;width:264px;text-transform:uppercase}
  .band-security{top:227px;width:401px;font-size:20px}
  .feature-list{position:absolute;left:20px;list-style:none;font-size:10.4px}
  .feature-list li{display:flex;align-items:center;height:16px}
  .feature-list svg{width:12px;height:12px;margin-right:16px;flex:none}
  .list-communities{top:83px}
  .list-features{top:174px}
  .unit-grid{position:absolute;left:20px;top:256px;display:grid;grid-template-columns:155px 120px;row-gap:6px;font-size:10.4px;list-style:none}
  .unit-grid li{display:flex;align-items:center;height:16px}
  .unit-grid svg{width:16px;height:16px;margin-right:9px;flex:none}
  .about-title{position:absolute;left:19px;top:310px;font-family:'Crimson Text',serif;font-weight:600;font-size:22px;color:var(--title);line-height:24px;padding-bottom:2px;border-bottom:1.5px solid var(--title)}
  .about-copy{position:absolute;left:19px;top:344px;width:412px;font-size:9.9px;line-height:13px}
  .about-copy p+p{margin-top:15px}
  .about-copy p.lead-line{margin-bottom:3px}
  .about-copy p.lead-line+p{margin-top:0}

  .emergency{position:absolute;left:31px;top:606px;color:#fff;font-size:10px;line-height:14.6px}
  .emergency h2{font-family:'Lato',sans-serif;font-weight:400;font-size:10.4px;letter-spacing:.2px;margin-bottom:1px}
  .emergency li{list-style:none}
  .emergency .hours{line-height:10.5px}
  .back-brand{right:42px;top:616px;font-size:13px;color:#fff}
  .contact{position:absolute;right:22px;top:641px;list-style:none;color:#fff;font-size:10px;text-align:right}
  .contact li{display:flex;justify-content:flex-end;align-items:center;height:16.5px}
  .contact svg{width:12px;height:12px;margin-left:6px}
</style>
</head>
<body>

<section class="page page--front" aria-label="Front page">
  <svg class="page-art" viewBox="0 0 570 734" aria-hidden="false">
    <defs>
      <linearGradient id="skylineTop" x1="0" y1="0" x2="1" y2="1">
        <stop offset="0" stop-color="#a9dce7"/>
        <stop offset="1" stop-color="#cdeef3"/>
      </linearGradient>
      <linearGradient id="streetScene" x1="0" y1="0" x2="0" y2="1">
        <stop offset="0" stop-color="#76aee3"/>
        <stop offset=".38" stop-color="#a6c9e8"/>
        <stop offset=".55" stop-color="#4d4f52"/>
        <stop offset=".78" stop-color="#6f6a63"/>
        <stop offset="1" stop-color="#b2b0aa"/>
      </linearGradient>
      <linearGradient id="skylineLow" x1="0" y1="0" x2="1" y2="0">
        <stop offset="0" stop-color="#9dc9ea"/>
        <stop offset="1" stop-color="#ffffff" stop-opacity="0"/>
      </linearGradient>
    </defs>
    <polygon points="0,0 363,0 133,118 0,84" fill="url(#skylineTop)" role="img" aria-label="Faint city skyline pattern"/>
    <polygon points="0,112 570,245 570,545 0,624" fill="var(--band)"/>
    <polygon points="0,134 570,252 570,537 0,599" fill="url(#streetScene)" role="img" aria-label="Street view of the dark brick apartment building with café at ground level"/>
    <rect x="0" y="630" width="172" height="104" fill="url(#skylineLow)" opacity=".7" role="img" aria-label="Faint city skyline pattern"/>
  </svg>
  <div class="brand-name front-brand">HARBOUR KIND LIVING</div>
  <h1 class="welcome">Welcome to Elmsbury</h1>
  <div class="welcome-copy">
    <p>Located in the heart of Elmsbury, our new 20 self-contained studio apartments which have a kitchen with fridge, small stove top and microwave. It has a single bed, tv, dining table and bathroom. Some apartments have small balconies, and some have decks overlooking the bustling suburb.</p>
    <p>Situated a 5 minute walk to Elmsbury Train Station, and other public transport.</p>
  </div>
</section>

<section class="page page--back" aria-label="Back page">
  <svg class="page-art" viewBox="0 0 570 734">
    <defs>
      <linearGradient id="roomScene" x1="0" y1="0" x2="1" y2="0">
        <stop offset="0" stop-color="#ffffff"/>
        <stop offset=".45" stop-color="#e2e2e2"/>
        <stop offset="1" stop-color="#a9a9a9"/>
      </linearGradient>
      <linearGradient id="skylineCorner" x1="0" y1="0" x2="1" y2="0">
        <stop offset="0" stop-color="#cbeef3"/>
        <stop offset="1" stop-color="#a6d8e6"/>
      </linearGradient>
      <linearGradient id="footerCity" x1="0" y1="0" x2="1" y2="0">
        <stop offset="0" stop-color="#63b2d6"/>
        <stop offset="1" stop-color="#4ea3cc"/>
      </linearGradient>
    </defs>
    <polygon points="240,25 570,180 570,520 360,548 300,420" fill="url(#roomScene)" role="img" aria-label="Bedroom with white bed beside a window with vertical balcony slats"/>
    <polygon points="227,0 570,0 570,170" fill="url(#skylineCorner)" role="img" aria-label="Faint city skyline pattern"/>
    <polygon points="0,588 570,505 570,516 0,597" fill="#eef3f5"/>
    <polygon points="0,597 570,516 570,734 0,734" fill="url(#footerCity)" role="img" aria-label="Blue panel with faint city skyline pattern"/>
  </svg>

  <div class="section-band band-communities">Communities &amp; Facilities</div>
  <ul class="feature-list list-communities">
    <li><svg viewBox="0 0 12 12" fill="none" stroke="#666" stroke-width="1"><path d="M3 1v10M1.5 1v3.5h3V1M8.5 1c-1.5 1-1.5 4 0 5v5"/></svg>Close to shops, cafes and public transport.</li>
    <li><svg viewBox="0 0 12 12" fill="none" stroke="#666" stroke-width="1"><path d="M6 10.5 1.5 6A2.6 2.6 0 0 1 6 2.8 2.6 2.6 0 0 1 10.5 6z"/><path d="M3 6h2l1-1.5 1 3 1-1.5h1"/></svg>Local GP Pracice and Dentistry.</li>
    <li><svg viewBox="0 0 12 12" fill="none" stroke="#777" stroke-width="1"><circle cx="6" cy="6" r="5"/><circle cx="6" cy="6" r="2.8"/><circle cx="6" cy="6" r=".8" fill="#777"/></svg>Commercial Space for Social Enterprise.</li>
  </ul>

  <div class="section-band band-features">Features &amp; Services</div>
  <ul class="feature-list list-features">
    <li><svg viewBox="0 0 12 12" fill="none" stroke="#222" stroke-width="1"><rect x="1" y="2" width="10" height="7.5"/><path d="M4 11h4"/></svg>24/7 Video - Intercom &amp; on site support.</li>
    <li><svg viewBox="0 0 12 12" fill="none" stroke="#222" stroke-width="1"><circle cx="5.5" cy="1.5" r="1" fill="#222"/><path d="M5.5 3v4h3l1 3"/><path d="M4 5.5a3 3 0 1 0 4 3.5"/></svg>Disability access walkways &amp; bathroom.</li>
    <li><svg viewBox="0 0 12 12" fill="none" stroke="#222" stroke-width="1"><circle cx="4" cy="2" r="1.3" fill="#222"/><path d="M4 4v4M2 6h4M4 8l-2 3M4 8l2 3M8 5l3 5M11 5l-3 5"/></svg>Trained &amp; expeienced Staff in psychosocial disability.</li>
  </ul>

  <div class="section-band band-security">Intercom, Security &amp; Air-Conditioning</div>
  <ul class="unit-grid">
    <li><svg viewBox="0 0 16 16" fill="none" stroke="#333" stroke-width="1"><path d="M1 8h14v2a3 3 0 0 1-3 3H4a3 3 0 0 1-3-3z"/><path d="M3 8V3a1.5 1.5 0 0 1 3 0M4 13l-1 2M12 13l1 2"/></svg>Accessible Bathroom</li>
    <li><svg viewBox="0 0 16 16" fill="none" stroke="#333" stroke-width="1"><rect x="3" y="3" width="10" height="11"/><path d="M5 6v8M8 6v8M11 6v8M3 6h10"/><path d="M1 1l14 14M15 1 1 15" stroke="#d33" stroke-width="1.6"/></svg>Without Balcony</li>
    <li><svg viewBox="0 0 16 16" fill="none" stroke="#333" stroke-width="1"><rect x="7" y="1" width="8" height="9"/><path d="M9 3v7M11 3v7M13 3v7"/><circle cx="4" cy="6" r="1.2" fill="#333"/><path d="M4 8v4M2 15l2-3 2 3M1 15h14"/></svg>Balcony Space Lvl 3</li>
    <li><svg viewBox="0 0 16 16" fill="none" stroke="#333" stroke-width="1"><path d="M3 8a5 5 0 0 1 10 0v7H3z"/><path d="M3 10h10M5 10v5M8 10v5M11 10v5M8 3v5"/></svg>Juliette Balcony</li>
  </ul>

  <h2 class="about-title">About KVAP</h2>
  <div class="about-copy">
    <p class="lead-line">KVAP stands for Key Village Access Plan.</p>
    <p>It is a Government initiative that provide billions of dollars in funding directly to individuals when they have a substantial disability that will impact how they complete daily activities either temporarily or for the rest of their lives.</p>
    <p>The KVAA (Key Village Access Agency) are the body that make the decision about who is eligible to become an KVAP participant and how much funding they will receive.</p>
    <p>It is not a welfare program but an Insurance Scheme to ensure that people with disabilities can have peace and security in life. Being able to live out their hopes and dreams is important for anyone and KVAP funding allows for a better quality of life for each participant.</p>
  </div>

  <div class="emergency">
    <h2>EMERGENCY CONTACT LIST</h2>
    <ul>
      <li>National Emergency Line: 000</li>
      <li>Elmsbury Police Station: (02) 5550 1140 &nbsp;( Open 24 hrs )</li>
      <li class="hours">Elmsbury Family Medical Centre: (02) 5550 2281<br>( Mon - Fri 9am - 9pm | Sat - Sun | 9am - 1pm )</li>
      <li>Riverside Council: (02) 5550 3900 &nbsp;( Open Mon - Fri | 8.30am - 5pm )</li>
      <li>Northgate General Hospital : (02) 5550 4411 &nbsp;( Open 24 hrs )</li>
      <li>BRSDA : (1300) 555 218 ( Open Mon - Fri | 9am - 5.30pm )</li>
    </ul>
  </div>

  <div class="brand-name back-brand">HARBOUR KIND LIVING</div>
  <ul class="contact">
    <li>1300 555 218<svg viewBox="0 0 12 12" fill="none" stroke="#fff" stroke-width="1"><circle cx="6" cy="6" r="5.4"/><path d="M4 3.2l1 1.6-.7.8a4 4 0 0 0 2 2l.8-.7 1.6 1-.6 1c-2.5 0-4.6-2.1-4.8-4.6z" fill="#fff"/></svg></li>
    <li>info@harbourkindliving.example<svg viewBox="0 0 12 12" fill="none" stroke="#fff" stroke-width="1"><rect x="1" y="2.5" width="10" height="7" fill="#fff"/><path d="M1 2.5l5 4 5-4" stroke="#59aad0"/></svg></li>
    <li>harbourkind_homes<svg viewBox="0 0 12 12" fill="none" stroke="#fff" stroke-width="1"><circle cx="6" cy="6" r="5.4"/></svg></li>
    <li>harbourkindliving.example<svg viewBox="0 0 12 12" fill="none" stroke="#fff" stroke-width="1"><circle cx="6" cy="6" r="5.4"/><ellipse cx="6" cy="6" rx="2.3" ry="5.4"/><path d="M.6 6h10.8M1.5 3.3h9M1.5 8.7h9"/></svg></li>
  </ul>
</section>

</body>
</html>
```